Corvanta Website Design (New Start Up Investment Management Firm)

We need a website designed. We have attached a Powerpoint with our proposed website content (which is quite minimal), the format is just a suggestion but we would like to see your alternative and improved ideas. We are a boutique investment firm so are looking for something sleek and professional. I have included on the last page of the attachment our brand colours and font styles as well as attaching our logo design. We would like the successful designer to design the website and build the buttons etc.

On the "Contact Us" page, we are open to suggestions on how best to show the map, whether is should be static or open a google maps page. We would like the phone number and email address to be set up so people can click on them on their phone and it calls us or emails us directly.

We would prefer not to have photos of landscapes on the site.
Our website is hosted on a Linux based website.

We would also like 3 links at the bottom of each page for links to pdfs:
- Disclaimer, Terms and Conditions of Web Site Use
- Stewardship
- Pillar III

Target Market(s)

Institutional Investors

Industry/Entity Type

Investment

Coding

Coded - Design and coding required

Number of Pages Required

3 page

Font styles to use
Other font styles liked:
• Logo: Lato, Text: Source Sans Pro

Colors

Designer to choose colors to be used in the design.

Requirements
Must have
• The website must use the colours and fonts on the last page of the attached powerpoint. I can't see an option to select the exact colour palette below so please look at the PPT.
• For others please see Project description.
Should not have
• Landscape photos

```html
<!DOCTYPE html>
<html lang="en">
<head>
<meta charset="utf-8">
<title>Corvanta Investment Management</title>
<link href="https://fonts.googleapis.com/css2?family=Lato:wght@300;400;700&display=swap" rel="stylesheet">
<style>
:root{
  --navy:#0b2d63;
  --navy-deep:#002d5f;
  --sky:#4a8fd6;
  --button:#6cb4ec;
  --grey:#5b5f66;
  --white:#ffffff;
  --hero-top:#f4f6f8;
  --hero-mid:#e6ecf1;
  --hero-low:#d3dde6;
}
*{margin:0;padding:0;box-sizing:border-box}
html,body{width:1200px;height:755px;overflow:hidden}
body{font-family:'Lato',sans-serif;position:relative;background:var(--hero-top)}
.hero{position:absolute;left:0;top:0;width:1200px;height:632px;
  background:radial-gradient(ellipse at 55% 30%,var(--hero-top) 0%,rgba(244,246,248,.9) 35%,transparent 70%),
  linear-gradient(115deg,var(--hero-low) 0%,var(--hero-mid) 35%,var(--hero-top) 60%,var(--hero-mid) 85%,var(--hero-low) 100%)}
.site-header{position:absolute;left:0;top:0;width:1200px;height:100px}
.brand{position:absolute;left:120px;top:28px;display:flex;align-items:center;gap:14px}
.brand-mark{width:58px;height:58px;background:var(--navy)}
.brand-text{display:flex;flex-direction:column;color:var(--navy);font-weight:400}
.brand-name{font-size:45px;line-height:44px;letter-spacing:1px}
.brand-tag{font-size:8.5px;letter-spacing:2.4px;margin-top:2px}
.main-nav{position:absolute;right:125px;top:48px;display:flex;gap:43px}
.main-nav a{font-size:16.5px;color:var(--navy);text-decoration:none;font-weight:400;letter-spacing:.2px}
.main-nav a.is-active{color:var(--sky)}
.welcome{position:absolute;left:0;top:195px;width:1200px;text-align:center}
.welcome h1{font-size:40px;font-weight:400;color:var(--sky);letter-spacing:.5px;line-height:52px}
.welcome .lead{margin:22px auto 0;width:870px;font-size:20px;line-height:29px;color:var(--navy)}
.welcome .body-copy{margin:16px auto 0;width:880px;font-size:16px;line-height:23px;color:var(--grey)}
.read-more{display:inline-block;margin-top:36px;width:153px;height:39px;line-height:39px;background:var(--button);color:var(--white);font-size:15.5px;text-decoration:none}
.site-footer{position:absolute;left:0;top:632px;width:1200px;height:123px;background:var(--navy-deep);color:var(--white)}
.doc-links{position:absolute;left:123px;top:29px;font-size:17px;display:flex;gap:12px}
.doc-links a{color:var(--white);text-decoration:none}
.doc-links span{opacity:.9}
.copyright{position:absolute;left:123px;top:64px;font-size:13.5px;font-weight:300}
.social{position:absolute;left:887px;top:33px;display:flex;gap:5px}
.social a{width:36px;height:36px;border:1.5px solid var(--white);border-radius:50%;display:block}
</style>
</head>
<body>
<div class="hero" role="img" aria-label="Pale upward view of glass office towers"></div>

<header class="site-header">
  <div class="brand">
    <div class="brand-mark"></div>
    <div class="brand-text">
      <span class="brand-name">CORVANTA</span>
      <span class="brand-tag">INVESTMENT MANAGEMENT</span>
    </div>
  </div>
  <nav class="main-nav">
    <a href="#" class="is-active">HOME</a>
    <a href="#">ABOUT US</a>
    <a href="#">APPROACH</a>
    <a href="#">SERVICES</a>
    <a href="#">CONTACT US</a>
  </nav>
</header>

<section class="welcome">
  <h1>WELCOME TO CORVANTA</h1>
  <p class="lead">Corvanta Investment Management was founded in 2016 with a clear vision to create an independent and nimble firm focused on generating superior risk-adjusted returns.</p>
  <p class="body-copy">Corvanta has designed an innovative investment approach which aims to harness the best elements of alternative investment management whilst reducing its recognised shortcomings. We are a performance and client focused firm, committed to building lasting relationships, treating our clients like partners rather than revenue streams.</p>
  <a href="#" class="read-more">READ MORE</a>
</section>

<footer class="site-footer">
  <div class="doc-links">
    <a href="#">Disclaimer</a><span>|</span>
    <a href="#">Terms and Conditions</a><span>|</span>
    <a href="#">Stewardship</a><span>|</span>
    <a href="#">Pillar III</a>
  </div>
  <p class="copyright">© 2017 Company Name&nbsp; All right reserved&nbsp; Term of Use</p>
  <div class="social">
    <a href="#" aria-label="Social profile 1"></a>
    <a href="#" aria-label="Social profile 2"></a>
    <a href="#" aria-label="Social profile 3"></a>
    <a href="#" aria-label="Social profile 4"></a>
    <a href="#" aria-label="Social profile 5"></a>
  </div>
</footer>
</body>
</html>
```